Etiketten für Gin
Zielgruppe
Wir vertreiben einen regionalen Gin mit Fichtennadeln.
Zielgruppe sind Gin-Trinker, Wanderer, Besucher und Bewohner der Bergischen Landes.
Aufgabenstellung
Benötigt wird ein zweiteiliges Etikett für eine 500 ml Flasche (Höhe 320 mm, Durchmesser ca. 75 mm). Datenblatt in der Anlage. Die Flasche wird einen schwarzen Stopfen bekommen,
Das vordere Etikett soll eine Größe von 80 mm (Breite) x 160 mm (Höhe) haben. Das Etikett für die Rückseite soll eine Größe von 60 mm (Breite) x 100 mm (Höhe) haben.
Aufgrund des schwarzen Stopfens wird ein Etikett mit/in schwarz favorisiert. Auf der Vorderseite soll unser Logo (bei den Dateien) abgebildet sein.
Pflichtangaben Vorderseite: auf dem vorderen Etikett müssen die Pflichtangaben zur Nettofüllmenge und zum Alkoholgehalt angegeben sein. Sprich, auf der Vorderseite muss 500 ml und 43 % untergebracht sein. Diese Pflichtangaben müssen zwingend eine Höhe von 4 mm haben (gesetzlich vorgeschrieben). Gleiches gilt für die Verkehrsbezeichnung Gin, die im Logo enthalten ist. Das Wort Gin muss ebenfalls eine Größe von mindestens 4 mm haben.
Auf dem rückwärtigen Etikett müssen folgende Pflichtangaben vorhanden sein:
Talwerk Brand
Lukas Dornfeld
Anton-Weller-Straße 27
51467 Bergisch Gladbach
Des Weiteren wären auf der Rückseite zwei Felder wünschenswert, in die man zum einen die Batch No. und zum anderen die Flaschennummer eintragen kann (Beispiel Bild 'Batch_Flasche'). Zudem ein weißes Feld, in dem später der EAN Code Ei gepflegt werden kann.
Als Text für die Rückseite:
Wo Natur auf Geschmack trifft
Das 'Bergische Gefühl' erleben Sie mit dem Talwerk Brand Gin. Lassen Sie einen naturverbundenen Tag zum Ausklang, beispielsweise nach einer Wanderung, noch einmal an Ihnen vorbeiziehen.
Erinnern Sie sich durch die bei der Herstellung geschmacksgebenden Botanicals von der Fichte an einen erholsamen Spaziergang durch die Wälder des Bergischen Landes.
Mehr Informationen unter
www.talwerk-brand.de
Druckdatenanlieferung laut Druckerei:
Dateiform..

```html
<!DOCTYPE html>
<html lang="de">
<head>
<meta charset="utf-8">
<title>Talwerk Brand Gin – Frontetikett</title>
<link href="https://fonts.googleapis.com/css2?family=Josefin+Sans:wght@400&family=Oswald:wght@400&family=Work+Sans:wght@400&family=Allura&display=swap" rel="stylesheet">
<style>
  :root {
    --canvas: #f2f2f2;
    --label-ground: #1a0406;
    --panel-black: #000000;
    --art-light: #3a3a3a;
    --art-dark: #050505;
    --ink-white: #ffffff;
    --pine-green: #6a9a2a;
  }
  html, body {
    margin: 0;
    padding: 0;
    width: 1200px;
    height: 1200px;
    overflow: hidden;
    background: var(--canvas);
  }
  .front-label {
    position: absolute;
    left: 107px;
    top: 60px;
    width: 986px;
    height: 1079px;
    background: var(--label-ground);
    overflow: hidden;
    color: var(--ink-white);
  }
  .brand-mark {
    position: absolute;
    left: 336px;
    top: 25px;
    width: 245px;
    height: 283px;
    display: flex;
    flex-direction: column;
    align-items: center;
    justify-content: center;
    gap: 22px;
  }
  .brand-mark__dot {
    width: 110px;
    height: 110px;
    border-radius: 50%;
    background: var(--pine-green);
  }
  .brand-mark__name {
    font-family: "Josefin Sans", sans-serif;
    font-weight: 400;
    font-size: 28px;
    letter-spacing: 1px;
    text-transform: uppercase;
    color: var(--ink-white);
    white-space: nowrap;
  }
  .product-name {
    position: absolute;
    left: 105px;
    top: 350px;
    width: 700px;
    margin: 0;
    text-align: center;
    font-family: "Josefin Sans", sans-serif;
    font-weight: 400;
    font-size: 78px;
    line-height: 1;
    letter-spacing: 1px;
    text-transform: uppercase;
    white-space: nowrap;
  }
  .art-panel {
    position: absolute;
    left: 191px;
    top: 431px;
    width: 795px;
    height: 648px;
    background: var(--panel-black);
  }
  .figure-illustration {
    position: absolute;
    left: 90px;
    top: 0;
    width: 705px;
    height: 648px;
    background: radial-gradient(ellipse at 62% 45%, var(--art-light) 0%, #1c1c1c 40%, var(--art-dark) 75%);
  }
  .category {
    position: absolute;
    left: 351px;
    top: 450px;
    width: 215px;
    display: flex;
    align-items: center;
    justify-content: space-between;
  }
  .category__dot {
    width: 14px;
    height: 14px;
    border-radius: 50%;
    background: var(--ink-white);
  }
  .category__word {
    font-family: "Oswald", sans-serif;
    font-weight: 400;
    font-size: 58px;
    line-height: 1;
    letter-spacing: 14px;
    margin-right: -14px;
    color: var(--pine-green);
  }
  .maker-signature {
    position: absolute;
    left: 100px;
    top: 680px;
    margin: 0;
    font-family: "Allura", cursive;
    font-size: 60px;
    line-height: 1;
    color: var(--ink-white);
    transform: rotate(-22deg);
    transform-origin: left center;
    white-space: nowrap;
  }
  .maker-signature small {
    display: block;
    font-size: 44px;
    margin-left: 120px;
    margin-bottom: -8px;
  }
  .legal {
    position: absolute;
    top: 1026px;
    font-family: "Work Sans", sans-serif;
    font-weight: 400;
    font-size: 38px;
    line-height: 1;
    color: var(--ink-white);
  }
  .legal--volume { left: 51px; }
  .legal--strength { left: 791px; }
</style>
</head>
<body>
  <main class="front-label">
    <div class="brand-mark">
      <span class="brand-mark__dot"></span>
      <span class="brand-mark__name">Talwerk Brand</span>
    </div>

    <h1 class="product-name">Talwerk Brand</h1>

    <div class="art-panel">
      <div class="figure-illustration" role="img" aria-label="Einlinige weiße Strichzeichnung eines lässig sitzenden Mannes auf schwarzem Grund"></div>
    </div>

    <div class="category">
      <span class="category__dot"></span>
      <span class="category__word">GIN</span>
      <span class="category__dot"></span>
    </div>

    <p class="maker-signature"><small>by</small>Lukas Dornfeld</p>

    <span class="legal legal--volume">500 ml</span>
    <span class="legal legal--strength">43 %</span>
  </main>
</body>
</html>
```